Jolly Paws Business Card Update

I have a business card which I love. I want to keep the same logo, colours, font and style. I want to upgrade the scripting and remove some elements and add others.
On the front side under Services - remove the existing wording and insert - Providing individual coaching strategies to create happy, healthy and social canine companions
Under Rebecca Thornbury amend the current wording to read: Qualified in Dog Behavioural Training, Natural Animal Healthcare and Animal Health Science
On the reverse side to remove the web address.

```html
<!DOCTYPE html>
<html lang="en">
<head>
<meta charset="utf-8">
<title>Jolly Paws Business Card Update</title>
<link href="https://fonts.googleapis.com/css2?family=Arimo:wght@400;700&family=Open+Sans:wght@300;400&display=swap" rel="stylesheet">
<style>
  :root {
    --blue-top: #039ddb;
    --blue-mid: #0c74bd;
    --blue-bottom: #2b3587;
    --red-edge: #68150f;
    --red-mid: #a0171a;
    --red-core: #e30d17;
    --cream: #efe6c4;
    --cream-light: #f8f1da;
    --ink: #111111;
    --white: #ffffff;
  }
  * { box-sizing: border-box; margin: 0; padding: 0; }
  html, body { width: 1200px; height: 1149px; overflow: hidden; background: var(--white); }
  body { position: relative; font-family: "Arimo", Arial, sans-serif; color: var(--white); }

  .card {
    position: absolute;
    width: 564px;
    height: 348px;
    overflow: hidden;
    background: linear-gradient(180deg, var(--blue-top) 0%, var(--blue-top) 18%, var(--blue-mid) 55%, var(--blue-bottom) 100%);
  }
  .card--existing-front { left: 13px; top: 102px; }
  .card--existing-back  { left: 591px; top: 100px; }
  .card--amended-front  { left: 36px; top: 645px; }
  .card--amended-back   { left: 613px; top: 647px; }

  .section-label {
    position: absolute;
    width: 300px;
    text-align: center;
    font-family: "Open Sans", Arial, sans-serif;
    font-weight: 700;
    font-size: 21px;
    color: var(--ink);
    letter-spacing: 0.5px;
  }
  .section-label--existing { left: 432px; top: 483px; }
  .section-label--amended  { left: 430px; top: 1037px; }

  /* Front side */
  .front__emblem {
    position: absolute;
    left: 214px; top: 59px;
    width: 132px; height: 132px;
    border-radius: 50%;
    background: var(--cream);
  }
  .front__name {
    position: absolute;
    left: 0; width: 100%;
    top: 192px;
    text-align: center;
    font-weight: 700;
    font-size: 37px;
    letter-spacing: 1px;
    color: var(--cream-light);
  }
  .front__tagline {
    position: absolute;
    left: 0; width: 100%;
    top: 234px;
    text-align: center;
    font-size: 17.5px;
    color: var(--white);
  }
  .front__swoosh { position: absolute; left: 0; top: 0; }
  .front__web {
    position: absolute;
    left: 0; width: 100%;
    top: 302px;
    text-align: center;
    font-size: 14px;
    color: var(--white);
  }

  /* Back side */
  .back__emblem {
    position: absolute;
    left: 76px; top: 60px;
    width: 112px; height: 112px;
    border-radius: 50%;
    background: var(--cream);
    display: flex; align-items: center; justify-content: center;
    text-align: center;
    font-weight: 700;
    font-size: 15px;
    line-height: 1.15;
    color: var(--red-edge);
  }
  .back__rule {
    position: absolute;
    left: 204px;
    width: 1px;
    background: var(--cream-light);
  }
  .back__rule--services { top: 64px; height: 103px; }
  .services { position: absolute; left: 224px; top: 62px; }
  .services__title { font-size: 17.5px; line-height: 20px; }
  .services__list { margin-top: 6px; font-size: 14.5px; line-height: 17.8px; }
  .services__statement {
    margin-top: 5px; margin-left: 4px;
    font-family: "Open Sans", Arial, sans-serif;
    font-weight: 300;
    font-size: 16.5px;
    line-height: 20.3px;
  }

  .back__band {
    position: absolute;
    left: 0; top: 196px;
    width: 100%; height: 22px;
    background: var(--cream);
    color: var(--ink);
    text-align: center;
    font-size: 15px;
    line-height: 22px;
    letter-spacing: -0.2px;
  }
  .back__contact-panel {
    position: absolute;
    left: 0; top: 218px;
    width: 100%; height: 130px;
    background: linear-gradient(90deg, var(--red-edge) 0%, var(--red-mid) 25%, var(--red-core) 50%, var(--red-mid) 75%, var(--red-edge) 100%);
  }

  .person {
    position: absolute;
    right: 260px;
    text-align: right;
    white-space: nowrap;
  }
  .person__name { font-size: 21px; line-height: 24px; }
  .person__role { font-size: 14px; line-height: 18px; margin-top: 1px; }
  .person__role--light {
    font-family: "Open Sans", Arial, sans-serif;
    font-weight: 300;
    font-size: 16px;
    line-height: 20.3px;
    margin-top: 1px;
  }
  .card--existing-back .person { top: 34px; }
  .card--amended-back .person { top: 24px; right: 258px; }

  .contact-rule { position: absolute; left: 314px; width: 1px; background: var(--cream-light); }
  .card--existing-back .contact-rule { top: 52px; height: 39px; }
  .card--amended-back .contact-rule { top: 48px; height: 60px; left: 315px; }

  .contacts { position: absolute; left: 322px; font-size: 17px; }
  .card--existing-back .contacts { top: 52px; }
  .card--amended-back .contacts { top: 63px; }
  .contact { display: flex; align-items: center; height: 21px; }
  .contact svg { width: 15px; height: 15px; margin-right: 6px; flex: none; }
</style>
</head>
<body>

  <!-- Existing: front -->
  <section class="card card--existing-front" aria-label="Existing card front">
    <div class="front__emblem"></div>
    <div class="front__name">JOLLY PAWS</div>
    <div class="front__tagline">HAPPY DOGS, HAPPY OWNERS</div>
    <svg class="front__swoosh" width="564" height="348" viewBox="0 0 564 348">
      <defs>
        <linearGradient id="redSweepA" x1="0" x2="1" y1="0" y2="0">
          <stop offset="0" stop-color="#68150f"/>
          <stop offset="0.25" stop-color="#a0171a"/>
          <stop offset="0.5" stop-color="#e30d17"/>
          <stop offset="0.75" stop-color="#a0171a"/>
          <stop offset="1" stop-color="#68150f"/>
        </linearGradient>
      </defs>
      <path d="M0 316 Q282 260 564 316 L564 348 L0 348 Z" fill="url(#redSweepA)"/>
      <path d="M0 316 Q282 260 564 316" fill="none" stroke="#efe6c4" stroke-width="3.5"/>
    </svg>
    <div class="front__web">www.jollypaws1.com</div>
  </section>

  <!-- Existing: back -->
  <section class="card card--existing-back" aria-label="Existing card back">
    <div class="back__emblem">JOLLY<br>PAWS</div>
    <div class="back__rule back__rule--services"></div>
    <div class="services">
      <div class="services__title">SERVICES</div>
      <div class="services__list">
        Behaviour Consults, Training,<br>
        Complex Skills and Walking Coaching,<br>
        Diet &amp; Nutrition, Massage,<br>
        Natural Healthcare Options
      </div>
    </div>
    <div class="back__band">Promoting communication and connection between dogs and their families</div>
    <div class="back__contact-panel">
      <div class="person">
        <div class="person__name">Rebecca Thornbury</div>
        <div class="person__role">Qualified Dog Behavioural Trainer<br>and Natural Animal Healthcare Consultant</div>
      </div>
      <div class="contact-rule"></div>
      <div class="contacts">
        <div class="contact">
          <svg viewBox="0 0 16 16"><circle cx="8" cy="8" r="7.5" fill="#f4ecd6"/><path d="M5 4.5h2l.8 2-1.2.9a5 5 0 0 0 2 2l.9-1.2 2 .8v2a1 1 0 0 1-1 1A7 7 0 0 1 4 5.5a1 1 0 0 1 1-1z" fill="#b3151a"/></svg>
          0400 162 375
        </div>
        <div class="contact">
          <svg viewBox="0 0 16 16"><circle cx="8" cy="8" r="7.5" fill="#f4ecd6"/><rect x="4" y="5.3" width="8" height="5.6" rx="0.8" fill="#b3151a"/><path d="M4.3 5.8 8 8.6l3.7-2.8" fill="none" stroke="#f4ecd6" stroke-width="0.9"/></svg>
          jollypaws1@pawmail.com
        </div>
      </div>
    </div>
  </section>

  <div class="section-label section-label--existing">EXISTING</div>

  <!-- Amended: front -->
  <section class="card card--amended-front" aria-label="Amended card front">
    <div class="front__emblem"></div>
    <div class="front__name">JOLLY PAWS</div>
    <div class="front__tagline">HAPPY DOGS, HAPPY OWNERS</div>
    <svg class="front__swoosh" width="564" height="348" viewBox="0 0 564 348">
      <defs>
        <linearGradient id="redSweepB" x1="0" x2="1" y1="0" y2="0">
          <stop offset="0" stop-color="#68150f"/>
          <stop offset="0.25" stop-color="#a0171a"/>
          <stop offset="0.5" stop-color="#e30d17"/>
          <stop offset="0.75" stop-color="#a0171a"/>
          <stop offset="1" stop-color="#68150f"/>
        </linearGradient>
      </defs>
      <path d="M0 316 Q282 260 564 316 L564 348 L0 348 Z" fill="url(#redSweepB)"/>
      <path d="M0 316 Q282 260 564 316" fill="none" stroke="#efe6c4" stroke-width="3.5"/>
    </svg>
  </section>

  <!-- Amended: back -->
  <section class="card card--amended-back" aria-label="Amended card back">
    <div class="back__emblem">JOLLY<br>PAWS</div>
    <div class="back__rule back__rule--services"></div>
    <div class="services">
      <div class="services__title">SERVICES</div>
      <div class="services__statement">
        Providing individual coaching strategies<br>
        to create happy, healthy and social<br>
        canine companions
      </div>
    </div>
    <div class="back__band">Promoting communication and connection between dogs and their families</div>
    <div class="back__contact-panel">
      <div class="person">
        <div class="person__name">Rebecca Thornbury</div>
        <div class="person__role--light">Qualified in Dog Behavioural Training<br>Natural Animal Healthcare and<br>Animal Health Science</div>
      </div>
      <div class="contact-rule"></div>
      <div class="contacts">
        <div class="contact">
          <svg viewBox="0 0 16 16"><circle cx="8" cy="8" r="7.5" fill="#f4ecd6"/><path d="M5 4.5h2l.8 2-1.2.9a5 5 0 0 0 2 2l.9-1.2 2 .8v2a1 1 0 0 1-1 1A7 7 0 0 1 4 5.5a1 1 0 0 1 1-1z" fill="#b3151a"/></svg>
          0400 162 375
        </div>
        <div class="contact">
          <svg viewBox="0 0 16 16"><circle cx="8" cy="8" r="7.5" fill="#f4ecd6"/><rect x="4" y="5.3" width="8" height="5.6" rx="0.8" fill="#b3151a"/><path d="M4.3 5.8 8 8.6l3.7-2.8" fill="none" stroke="#f4ecd6" stroke-width="0.9"/></svg>
          jollypaws1@pawmail.com
        </div>
      </div>
    </div>
  </section>

  <div class="section-label section-label--amended">AMMENDED</div>

</body>
</html>
```